Simplified Double Diamond Diagram for Book

I need a simplified version of the Double Diamond Diagram for a book I am working on. I would like to represent the diagram with the following image/text:
- Two diamonds connected (as in each of the sample photos)
- Inclusion of "Diverge" "Converge" above each of the sides of the diamonds as shown in sample image 1 - without elaborative text
- Inclusion of "Problem" and "Solution" in each diamond as is shown in the example image 2
- I need a color version and black/white version of the image that can be turned into a mono-color version in the book.

```html
<!DOCTYPE html>
<html lang="en">
<head>
<meta charset="utf-8">
<title>Double Diamond Diagram – Colour and Mono Versions</title>
<link rel="stylesheet" href="https://fonts.googleapis.com/css2?family=Poppins:wght@600;700&display=swap">
<style>
  :root {
    --page: #ffffff;
    --ink: #000000;
    --muted-ink: #666666;
    --guide: #555555;
    --problem-diverge: #1976d2;
    --problem-converge: #62a8eb;
    --problem-edge: #0d2b55;
    --solution-diverge: #f5973f;
    --solution-converge: #f3ba87;
    --solution-edge: #e8590c;
    --mono-fill: #cccccc;
    --on-colour: #ffffff;
  }
  html, body {
    margin: 0;
    padding: 0;
    width: 1200px;
    height: 1200px;
    overflow: hidden;
    background: var(--page);
  }
  .canvas {
    display: block;
    width: 1200px;
    height: 1200px;
  }
  .phase-label {
    font-family: "Poppins", sans-serif;
    font-weight: 700;
    font-size: 19px;
    fill: var(--ink);
    text-anchor: middle;
    dominant-baseline: middle;
    letter-spacing: 0.2px;
  }
  .stage-label {
    font-family: "Poppins", sans-serif;
    font-weight: 700;
    font-size: 19px;
    text-anchor: middle;
    dominant-baseline: middle;
  }
  .stage-label--light { fill: var(--on-colour); }
  .stage-label--dark { fill: var(--ink); }
  .stage-label--muted { fill: var(--muted-ink); }

  .half--problem-diverge { fill: var(--problem-diverge); }
  .half--problem-converge { fill: var(--problem-converge); }
  .half--solution-diverge { fill: var(--solution-diverge); }
  .half--solution-converge { fill: var(--solution-converge); }
  .half--mono { fill: var(--mono-fill); }

  .outline { fill: none; stroke-width: 3; stroke-linejoin: miter; }
  .outline--problem { stroke: var(--problem-edge); }
  .outline--solution { stroke: var(--solution-edge); }
  .outline--mono { stroke: var(--ink); }

  .axis {
    stroke: var(--guide);
    stroke-width: 2.5;
    stroke-dasharray: 8 8;
  }
  .axis--inner { stroke-width: 2; }
  .node { fill: var(--ink); }
</style>
</head>
<body>
<svg class="canvas" viewBox="0 0 1500 1500" xmlns="http://www.w3.org/2000/svg" role="img" aria-label="Double Diamond diagram in colour and monochrome versions">

  <!-- Row 1: colour -->
  <g class="diagram diagram--colour">
    <g transform="translate(217 118)">
      <line class="axis" x1="0" y1="-60" x2="0" y2="387"/>
      <polygon class="half--problem-diverge" points="0,0 -158,157 0,314"/>
      <polygon class="half--problem-converge" points="0,0 158,157 0,314"/>
      <polygon class="outline outline--problem" points="0,0 158,157 0,314 -158,157"/>
      <text class="phase-label" transform="translate(-93 48) rotate(-45)">DIVERGE</text>
      <text class="phase-label" transform="translate(103 57) rotate(45)">CONVERGE</text>
    </g>
    <g transform="translate(537 118)">
      <line class="axis" x1="0" y1="-60" x2="0" y2="387"/>
      <polygon class="half--solution-diverge" points="0,0 -157,157 0,314"/>
      <polygon class="half--solution-converge" points="0,0 158,157 0,314"/>
      <polygon class="outline outline--solution" points="0,0 158,157 0,314 -157,157"/>
      <text class="phase-label" transform="translate(-93 48) rotate(-45)">DIVERGE</text>
      <text class="phase-label" transform="translate(103 57) rotate(45)">CONVERGE</text>
    </g>
    <circle class="node" cx="60" cy="275" r="6"/>
    <circle class="node" cx="378" cy="275" r="6"/>
    <circle class="node" cx="695" cy="275" r="6"/>
  </g>

  <g class="diagram diagram--colour-labelled">
    <g transform="translate(962 118)">
      <line class="axis" x1="0" y1="-60" x2="0" y2="387"/>
      <polygon class="half--problem-diverge" points="0,0 -158,157 0,314"/>
      <polygon class="half--problem-converge" points="0,0 158,157 0,314"/>
      <polygon class="outline outline--problem" points="0,0 158,157 0,314 -158,157"/>
      <text class="phase-label" transform="translate(-93 48) rotate(-45)">DIVERGE</text>
      <text class="phase-label" transform="translate(103 57) rotate(45)">CONVERGE</text>
      <text class="stage-label stage-label--light" x="4" y="150">PROBLEM</text>
    </g>
    <g transform="translate(1281 118)">
      <line class="axis" x1="2" y1="-60" x2="2" y2="387"/>
      <polygon class="half--solution-diverge" points="0,0 -157,157 0,314"/>
      <polygon class="half--solution-converge" points="0,0 158,157 0,314"/>
      <polygon class="outline outline--solution" points="0,0 158,157 0,314 -157,157"/>
      <text class="phase-label" transform="translate(-93 48) rotate(-45)">DIVERGE</text>
      <text class="phase-label" transform="translate(103 57) rotate(45)">CONVERGE</text>
      <text class="stage-label stage-label--light" x="-2" y="150">SOLUTION</text>
    </g>
    <circle class="node" cx="804" cy="275" r="6"/>
    <circle class="node" cx="1122" cy="275" r="6"/>
    <circle class="node" cx="1439" cy="275" r="6"/>
  </g>

  <!-- Row 2: grey fill -->
  <g class="diagram diagram--grey">
    <g transform="translate(216 624)">
      <polygon class="half--mono" points="0,0 -158,158 0,316"/>
      <polygon class="outline outline--mono" points="0,0 158,158 0,316 -158,158"/>
      <text class="phase-label" transform="translate(-93 48) rotate(-45)">DIVERGE</text>
      <text class="phase-label" transform="translate(103 57) rotate(45)">CONVERGE</text>
    </g>
    <g transform="translate(537 624)">
      <polygon class="half--mono" points="0,0 -159,158 0,316"/>
      <polygon class="outline outline--mono" points="0,0 158,158 0,316 -159,158"/>
      <text class="phase-label" transform="translate(-93 48) rotate(-45)">DIVERGE</text>
      <text class="phase-label" transform="translate(103 57) rotate(45)">CONVERGE</text>
    </g>
  </g>

  <g class="diagram diagram--grey-labelled">
    <g transform="translate(963 624)">
      <polygon class="half--mono" points="0,0 -159,158 0,316"/>
      <polygon class="outline outline--mono" points="0,0 158,158 0,316 -159,158"/>
      <text class="phase-label" transform="translate(-93 48) rotate(-45)">DIVERGE</text>
      <text class="phase-label" transform="translate(103 57) rotate(45)">CONVERGE</text>
      <text class="stage-label stage-label--dark" x="4" y="151">PROBLEM</text>
    </g>
    <g transform="translate(1284 624)">
      <polygon class="half--mono" points="0,0 -158,158 0,316"/>
      <polygon class="outline outline--mono" points="0,0 158,158 0,316 -158,158"/>
      <text class="phase-label" transform="translate(-93 48) rotate(-45)">DIVERGE</text>
      <text class="phase-label" transform="translate(103 57) rotate(45)">CONVERGE</text>
      <text class="stage-label stage-label--dark" x="-2" y="151">SOLUTION</text>
    </g>
  </g>

  <!-- Row 3: outline only -->
  <g class="diagram diagram--outline">
    <g transform="translate(216 1133)">
      <line class="axis axis--inner" x1="-1" y1="4" x2="-1" y2="312"/>
      <polygon class="outline outline--mono" points="0,0 158,158 0,316 -158,158"/>
      <text class="phase-label" transform="translate(-93 48) rotate(-45)">DIVERGE</text>
      <text class="phase-label" transform="translate(103 57) rotate(45)">CONVERGE</text>
    </g>
    <g transform="translate(537 1133)">
      <line class="axis axis--inner" x1="-1" y1="4" x2="-1" y2="312"/>
      <polygon class="outline outline--mono" points="0,0 158,158 0,316 -159,158"/>
      <text class="phase-label" transform="translate(-93 48) rotate(-45)">DIVERGE</text>
      <text class="phase-label" transform="translate(103 57) rotate(45)">CONVERGE</text>
    </g>
  </g>

  <g class="diagram diagram--outline-labelled">
    <g transform="translate(963 1133)">
      <line class="axis axis--inner" x1="0" y1="4" x2="0" y2="312"/>
      <polygon class="outline outline--mono" points="0,0 158,158 0,316 -159,158"/>
      <text class="phase-label" transform="translate(-93 48) rotate(-45)">DIVERGE</text>
      <text class="phase-label" transform="translate(103 57) rotate(45)">CONVERGE</text>
      <text class="stage-label stage-label--muted" x="4" y="151">PROBLEM</text>
    </g>
    <g transform="translate(1284 1133)">
      <line class="axis axis--inner" x1="-1" y1="4" x2="-1" y2="312"/>
      <polygon class="outline outline--mono" points="0,0 158,158 0,316 -158,158"/>
      <text class="phase-label" transform="translate(-93 48) rotate(-45)">DIVERGE</text>
      <text class="phase-label" transform="translate(103 57) rotate(45)">CONVERGE</text>
      <text class="stage-label stage-label--muted" x="-2" y="151">SOLUTION</text>
    </g>
  </g>

</svg>
</body>
</html>
```